Business card-Tales From The Harbor Gate

Looking for a business card. I have a website I designed "TalesFromTheHarborGate.com I am not a graphic artist and may at some point need help with my website too. Used the font "Hello Stockholm" on my website. I am a writer, looking to get published. Liked the "feel" of the cover below. No cliche typwriters, keyboards, pens. - Edgar P. Lindqvist
Updates

Not 100% sold on needing the owls, just a place to begin. I probably sounds like I'm going to be a pain to work with, I was a video production manager for 15+ years. When I would give an editor or graphic artist a project and let them run with it, the results were typically beyond my expectations. I give the idea then as the artists touch it, and adds value I could never bring to the project. Make something you would be proud of, don't try to second-guess me.

Target Market(s)

Agents, publishers, people I want to buy my book once I get it published

Industry/Entity Type

Publishing

Contact Information for Business Card

Edgar P. Lindqvist
TalesFromTheHarborGate.com
Phone #-TBD
Edgar@TalesFromTheHarbroGate.com
Maybe address; 418 N. 7th St Cheyenne, WY 82947

Colors
fcca95
3277b5

Requirements
Must have
• I like the "chromatic" feel of the attached cover. As you can see from my website, I'm an owl fan. Those pictures I took and do own the rights too. Not sure if they are approritae for a business card.
Should not have
• Cliche I like the "chromatic" feel of the attached book cover.
• I will need help with my website at some point too. I want the website to be easy for me to update, and reflect the same feel as the card. I write adventure, mystery. I have romance in my books too...Adventure of Romance, Romance of adventure, I am not sure but those words were like by an author firned of mine. They are rather "light" reading too.

```html
<!DOCTYPE html>
<html lang="en">
<head>
<meta charset="utf-8">
<title>Tales From The Harbor Gate – Business Card</title>
<link href="https://fonts.googleapis.com/css2?family=Kaushan+Script&family=Oswald:wght@300;400;500&display=swap" rel="stylesheet">
<style>
  :root {
    --page-bg: #ece8e2;
    --ink: #1f2430;
    --name-blue: #3a64a0;
    --icon-blue: #3e68a6;
    --brand-peach: #fcca95;
    --brand-blue: #3277b5;
    --deep-blue: #2f4f9e;
    --sky-light: #dfe9f1;
    --sky-mid: #b9cfe0;
    --hills: #8fa9c4;
    --lake: #7fb3cf;
    --owl-warm: #9c8468;
    --owl-cool: #8d9cb6;
  }
  * { box-sizing: border-box; margin: 0; padding: 0; }
  html, body {
    width: 1200px; height: 750px; overflow: hidden;
    background: var(--page-bg);
  }
  .sheet {
    position: relative; width: 1200px; height: 750px;
  }
  .card {
    position: absolute; top: 195px;
    width: 488px; height: 314px;
    overflow: hidden;
    box-shadow: 4px 5px 8px rgba(0,0,0,0.35);
  }
  .card--front { left: 77px; }
  .card--back { left: 639px; }

  .landscape {
    position: absolute; inset: 0;
    background:
      linear-gradient(180deg, rgba(255,255,255,0) 55%, rgba(143,178,140,0.35) 100%),
      radial-gradient(ellipse 60% 30% at 30% 72%, var(--lake) 0%, rgba(127,179,207,0) 70%),
      radial-gradient(ellipse 70% 45% at 25% 60%, var(--hills) 0%, rgba(143,169,196,0) 75%),
      linear-gradient(180deg, var(--sky-light) 0%, var(--sky-mid) 45%, #c7d7e4 100%);
  }
  .owl-photo {
    position: absolute; right: 0; top: 56px;
    width: 138px; height: 258px;
    border-radius: 30px 0 0 0;
    background: linear-gradient(180deg, var(--owl-warm) 0%, #a89a88 45%, var(--owl-cool) 100%);
    opacity: 0.9;
  }

  .front-content {
    position: absolute; inset: 0;
    font-family: "Oswald", sans-serif; color: var(--ink);
  }
  .holder-name {
    position: absolute; left: 39px; top: 34px;
    font-family: "Kaushan Script", cursive;
    font-size: 34px; color: var(--name-blue); letter-spacing: 0.5px;
  }
  .site-name {
    position: absolute; left: 39px; top: 98px;
    font-size: 17px; font-weight: 500;
  }
  .contact-line {
    position: absolute; left: 38px;
    display: flex; align-items: center; gap: 8px;
    font-size: 15px; font-weight: 300;
  }
  .contact-line--email { top: 138px; }
  .contact-line--phone { top: 168px; }
  .contact-icon { width: 25px; height: 25px; flex: none; }
  .address {
    position: absolute; left: 40px; top: 250px;
    font-size: 14px; font-weight: 300;
  }

  .back-field {
    position: absolute; inset: 0;
    background:
      radial-gradient(ellipse 60% 25% at 55% 68%, rgba(47,79,158,0.6) 0%, rgba(47,79,158,0) 70%),
      radial-gradient(ellipse 40% 15% at 30% 12%, rgba(40,70,150,0.5) 0%, rgba(40,70,150,0) 70%),
      linear-gradient(180deg, var(--brand-blue) 0%, #3568b0 55%, var(--deep-blue) 100%);
  }
  .back-url {
    position: absolute; left: 0; right: 0; top: 140px;
    text-align: center;
    font-family: "Oswald", sans-serif; font-weight: 400;
    font-size: 22px; color: var(--brand-peach);
  }
</style>
</head>
<body>
<main class="sheet">
  <section class="card card--front">
    <div class="landscape" role="img" aria-label="Soft hazy photo of mountains over a lake under a cloudy sky"></div>
    <div class="owl-photo" role="img" aria-label="Photo of a great horned owl"></div>
    <div class="front-content">
      <h1 class="holder-name">Edgar P. Lindqvist</h1>
      <p class="site-name">TalesFromTheHarborGate.com</p>
      <p class="contact-line contact-line--email">
        <svg class="contact-icon" viewBox="0 0 25 25" aria-hidden="true">
          <circle cx="12.5" cy="12.5" r="12.5" fill="var(--icon-blue)"/>
          <rect x="6" y="8" width="13" height="9" fill="none" stroke="#fff" stroke-width="1.4"/>
          <path d="M6 8 L12.5 13.5 L19 8" fill="none" stroke="#fff" stroke-width="1.4"/>
        </svg>
        Edgar@TalesFromTheHarbroGate.com
      </p>
      <p class="contact-line contact-line--phone">
        <svg class="contact-icon" viewBox="0 0 25 25" aria-hidden="true">
          <circle cx="12.5" cy="12.5" r="12.5" fill="var(--icon-blue)"/>
          <rect x="8.5" y="5" width="8" height="15" rx="1.5" fill="var(--brand-peach)"/>
          <rect x="10" y="7" width="5" height="5" fill="var(--icon-blue)"/>
          <circle cx="12.5" cy="16.5" r="1.2" fill="var(--icon-blue)"/>
        </svg>
        307 555 0148
      </p>
      <p class="address">418 N. 7th St Cheyenne, WY 82947</p>
    </div>
  </section>

  <section class="card card--back">
    <div class="back-field" role="img" aria-label="Blue tinted photo of misty mountains"></div>
    <p class="back-url">www.talesfromtheharborgate.com</p>
  </section>
</main>
</body>
</html>
```